Tavington Inc 1 pg brochure for entrepreneurs

We need a one page brochure (2 sided) designed for a finance and strategy consulting company called Tavington Inc. which does work in Canada and the United States currently. This company works with entrepreneurs, helping them to establish finance operations, evaluate their financial infomation and apply insight from it to business strategies. Essentially we help entrepreneurs grow their business ... we take care of their finance needs and give them sound business advice ... allowing them to focus on their core business and business strategy.

This one page brochure is meant to caputure what services we provide but also positon that we are also entrepreneurs and we understand how entrepreneurs think .... we not only bring technical competence but cultural insight in this regard as well. We understand how nimble and stealth an entrepreneur's business is so we don't gouge them with expensive consulting fees. We don't want to look like a massive corporation ...we want to look professional, smart and reliable. We want to reflect that we are entrepreneural ourselves even in fact that we have a niche offering that is totally targeted to businesses of this nature.

Major emphasis points for the piece are
1) our core values, this could be a side bar or box
2) the credentials of our founder, he is technically competent and an entrepreneur himself (we have his picture to include)
3) our offerings, what we can do for a company, the client quotes provided are a good illustration of what we offer, the relief we provide a client and of what value we provide - make sure you read these, this could also be a side bar or box, some kind of special call out so the service offerings are very clear

The brochure needs to be editable, so in a format that we can work with it for future, if we need to make updates, one that we can use in Microsoft word and convert to a PDF format. It will be emailed to people (in pdf) and also brought to meetings.

We have a new logo and this design should be an extenstion of it from a colour, look and feel perspective. The piece should also be clean and not too copy heavy so we encourage use of sub-heads, whitespace, etc.

When we send this piece out or hand it to someone, the impression should be "I am comfortable with Tavington Inc. they can help me and are people who get me, people I can trust to work closely with me on my business who are personally vested in my success".
Updates

Hello all, thank you for sumitting designs, there is some great work here.  A few changes/requests ...

Pls add the following headline on the front page right off the top

Entrepreneurs helping entrepreneurs, providing strategic financial services

Can we put Services on the front page? and call them out with treatment in a text box or with something strong that creates emphasis

Can the quote pls be broken up as opposed to one long list of 6 quotes? They can be floated throughout the piece, we can use less of them (or not) and put them on the front and back of the brochure? 

Also looking for the final product to be a little more bold in colour ...

Thx all, let us know if you have questions

Target Market(s)

Individuals (CEO) who runs their own established, yet growing business, who needs a business-minded CFO

Industry/Entity Type

Financial

Requirements
Must have
• Must have photo of founder, include his name and credentials under photo
All copy provide must be included
If not sure of a headline put in dummy text and we will provide headline or sub head copy
Should not have
• Fonts to be clean, no serif fonts. Should compliment logo, not the same font exactly but easily replicable in Microsoft Word and complimentary
No illustrations or cliche clip art

```html
<!DOCTYPE html>
<html lang="en">
<head>
<meta charset="utf-8">
<title>Tavington Inc – Brochure</title>
<link rel="stylesheet" href="https://fonts.googleapis.com/css2?family=Open+Sans:wght@400;600;700;800&display=swap">
<style>
  :root {
    --navy: #2d4fa6;
    --cyan: #4aafcc;
    --ink: #2c2f38;
    --grey: #e6e7e9;
    --grey-light: #f1f2f3;
    --paper: #ffffff;
    --backdrop: #565a70;
  }
  * { box-sizing: border-box; margin: 0; padding: 0; }
  html, body { width: 1200px; height: 848px; overflow: hidden; }
  body {
    background: var(--backdrop);
    font-family: "Open Sans", sans-serif;
    color: var(--ink);
    position: relative;
  }
  .page {
    position: absolute;
    top: 20px;
    width: 540px;
    height: 808px;
    background: var(--paper);
    padding: 20px 28px;
    overflow: hidden;
  }
  .page--front { left: 44px; }
  .page--back { left: 616px; }
  .page__content { position: relative; z-index: 1; }

  /* brand lockup */
  .brand { display: flex; align-items: center; gap: 12px; }
  .brand__mark { width: 58px; height: 58px; border: 4px solid var(--navy); flex: none; }
  .brand__name { font-size: 28px; font-weight: 700; color: var(--navy); line-height: 1; }
  .brand__tagline { font-size: 11px; color: var(--cyan); letter-spacing: .04em; margin-top: 3px; }
  .brand-rule { height: 12px; width: 260px; background: var(--navy); margin: 6px 0 0 70px; }

  .band {
    display: inline-block;
    background: var(--navy);
    color: #fff;
    font-weight: 800;
    font-size: 15px;
    letter-spacing: .06em;
    text-transform: uppercase;
    padding: 2px 60px 2px 12px;
    margin: 10px 0 6px;
  }
  .body-copy { font-size: 8px; line-height: 1.4; }
  .body-copy + .body-copy { margin-top: 5px; }

  .quote {
    background: var(--cyan);
    color: #fff;
    font-size: 9px;
    line-height: 1.45;
    padding: 9px 12px 9px 32px;
    position: relative;
  }
  .quote::before {
    content: "\201D";
    position: absolute;
    left: 9px; top: 2px;
    font-size: 28px;
    font-weight: 800;
    color: var(--navy);
    line-height: 1;
  }
  .quote--strip { margin: 8px -28px 8px 0; padding: 5px 14px 5px 32px; }
  .quote--strip::before { top: 0; }

  /* front page */
  .who { display: grid; grid-template-columns: 100px 1fr 160px; gap: 12px; align-items: start; }
  .founder-photo {
    width: 100px; height: 118px;
    border: 3px solid var(--navy);
    background: linear-gradient(160deg, #5b5149 0%, #241f1e 60%, #1b1c2a 100%);
  }
  .split { display: grid; grid-template-columns: 1fr 200px; gap: 14px; align-items: start; margin-top: 4px; }
  .quote--closing { width: 300px; margin-top: 12px; font-size: 10.5px; padding: 11px 14px 11px 36px; }

  /* back page */
  .brand--back { margin-left: 20px; }
  .subline {
    background: var(--cyan);
    color: #fff;
    font-size: 7.5px;
    padding: 3px 10px 3px 34px;
    margin: 10px -28px 14px 0;
    position: relative;
  }
  .subline::before {
    content: "\201D"; position: absolute; left: 12px; top: -3px;
    font-size: 20px; font-weight: 800; color: var(--navy);
  }
  .columns { display: grid; grid-template-columns: 1fr 1fr; gap: 14px; }
  .columns .band { display: block; margin: 0 0 8px; padding-right: 12px; font-size: 14px; }
  .tick-list { list-style: none; }
  .tick-list li {
    display: flex; gap: 8px;
    background: var(--grey);
    font-size: 8.5px; line-height: 1.45;
    padding: 6px 8px;
    margin-bottom: 6px;
  }
  .tick-list svg { flex: none; width: 11px; height: 11px; margin-top: 2px; }
  .contact { margin-top: 26px; display: flex; flex-direction: column; gap: 10px; font-style: normal; }
  .contact__row { display: flex; align-items: center; gap: 8px; }
  .contact__icon {
    width: 28px; height: 28px; background: var(--cyan);
    display: flex; align-items: center; justify-content: center; flex: none;
  }
  .contact__text {
    background: var(--grey);
    font-size: 11px; padding: 6px 12px;
    min-width: 220px;
    white-space: nowrap;
  }
  .back-footer { position: absolute; left: 0; right: 0; bottom: 0; height: 130px; background: var(--grey-light); z-index: 0; }
</style>
</head>
<body>

<section class="page page--front">
  <div class="page__content">
    <header>
      <div class="brand">
        <div class="brand__mark"></div>
        <div>
          <div class="brand__name">Tavington Inc</div>
          <div class="brand__tagline">Aligning Finance and Vision</div>
        </div>
      </div>
      <div class="brand-rule"></div>
    </header>

    <h2 class="band">Mission</h2>
    <p class="body-copy">Tavington Inc. provides strategic financial services to entrepreneurs. We are entrepreneurs assisting entrepreneurs. By engaging us, entrepreneurs can regularly access senior executive financial acumen and strategic discipline without having to hire a full-time financial executive or overspend on third-party service providers who are transactional in nature.</p>

    <h2 class="band">Who are we?</h2>
    <div class="who">
      <div class="founder-photo" role="img" aria-label="Portrait photograph of founder Mark Hadley"></div>
      <div>
        <p class="body-copy">Tavington Inc. evolved out of the companies, partnerships and relationships that Mark Hadley, its founder, has nurtured and built over the last 22 years. Mr. Hadley, the founder of Tavington, is an entrepreneur himself having built his own companies and managed several successful investment funds whose mandates were to invest in entrepreneurial growth companies.</p>
        <p class="body-copy">Over his career, he has worked extensively with entrepreneurs like himself who have struggled to build an experienced and engaged executive management team. Common comments from visionary entrepreneurs (which Tavington Inc. helps address) include:</p>
      </div>
      <blockquote class="quote">I need a financial executive to integrate my operating objectives with my financial ones. They are not aligned and are working against each other.</blockquote>
    </div>

    <blockquote class="quote quote--strip">If I could hire my equal in a financial capacity, my executive team would be complete.</blockquote>

    <div class="split">
      <div>
        <p class="body-copy">Mr. Hadley has a proven track record of developing and implementing strategic corporate policy. His experience and education is in corporate finance, portfolio management and building businesses. He is a registered Portfolio Manager. He also has earned an MBA from Lakeshore University (1995) and is a Chartered Financial Analyst (CFA, 1999). He applies this competence to valuating an entrepreneur's vision and corporate strategies and assisting in translating them into higher growth, improved efficiency and higher profitability.</p>
        <p class="body-copy">He has extensive experience in public and private, debt and equity capital markets, involving raising, managing and investing capital and completing corporate transactions. He has evaluated hundreds of corporate business strategies for potential investment. Other core skills include financial and tax analysis, working with high-performing investment teams, managing financial and accounting functions, designing and implementing operational and compliance systems.</p>
      </div>
      <blockquote class="quote">I need a financial executive who gets the numbers, can think strategically and translate that combined expertise and understanding into forward-looking corporate strategies.</blockquote>
    </div>

    <blockquote class="quote quote--closing">I would be a billionaire if I could implement better financial systems and apply strategic discipline.</blockquote>
  </div>
</section>

<section class="page page--back">
  <div class="back-footer"></div>
  <div class="page__content">
    <header>
      <div class="brand brand--back">
        <div class="brand__mark"></div>
        <div>
          <div class="brand__name">Tavington Inc</div>
          <div class="brand__tagline">Aligning Finance and Vision</div>
        </div>
      </div>
      <div class="brand-rule"></div>
    </header>

    <p class="subline">I need a financial executive who understands the inherent makeup of an entrepreneur.</p>

    <div class="columns">
      <div>
        <h2 class="band">Core values</h2>
        <ul class="tick-list">
          <li><svg viewBox="0 0 12 12"><rect width="12" height="12" fill="#2d4fa6"/><path d="M3 6.2l2 2 4-4.4" stroke="#fff" stroke-width="1.6" fill="none"/></svg><span>We love working with entrepreneurs because they like <b>adventure</b>. We understand the high energy, creativity and passion required to take high risks and achieve a corporate vision.</span></li>
          <li><svg viewBox="0 0 12 12"><rect width="12" height="12" fill="#2d4fa6"/><path d="M3 6.2l2 2 4-4.4" stroke="#fff" stroke-width="1.6" fill="none"/></svg><span>We like entrepreneurs because they are focused on <b>achievement</b>. They are "can-do" people who take action.</span></li>
          <li><svg viewBox="0 0 12 12"><rect width="12" height="12" fill="#2d4fa6"/><path d="M3 6.2l2 2 4-4.4" stroke="#fff" stroke-width="1.6" fill="none"/></svg><span>We like entrepreneurs because their business relationships are like <b>family</b>. Entrepreneurs are personally invested and value personal relationships with amazing people.</span></li>
          <li><svg viewBox="0 0 12 12"><rect width="12" height="12" fill="#2d4fa6"/><path d="M3 6.2l2 2 4-4.4" stroke="#fff" stroke-width="1.6" fill="none"/></svg><span>We like entrepreneurs because they work hard and live well. <b>Health and wellness</b> is as important as financial success, and most of all having fun is central to the mind set of most successful entrepreneurs.</span></li>
        </ul>
      </div>
      <div>
        <h2 class="band">Services</h2>
        <ul class="tick-list">
          <li><svg viewBox="0 0 12 12"><rect width="12" height="12" fill="#2d4fa6"/><path d="M3 6.2l2 2 4-4.4" stroke="#fff" stroke-width="1.6" fill="none"/></svg><span>We work intimately with our clients to determine their corporate and personal objectives.</span></li>
          <li><svg viewBox="0 0 12 12"><rect width="12" height="12" fill="#2d4fa6"/><path d="M3 6.2l2 2 4-4.4" stroke="#fff" stroke-width="1.6" fill="none"/></svg><span>We evaluate corporate strategies and assist in aligning them with financial ones.</span></li>
          <li><svg viewBox="0 0 12 12"><rect width="12" height="12" fill="#2d4fa6"/><path d="M3 6.2l2 2 4-4.4" stroke="#fff" stroke-width="1.6" fill="none"/></svg><span>We assist in budgeting, investing, financial forecasting and analysis and asset management.</span></li>
          <li><svg viewBox="0 0 12 12"><rect width="12" height="12" fill="#2d4fa6"/><path d="M3 6.2l2 2 4-4.4" stroke="#fff" stroke-width="1.6" fill="none"/></svg><span>We develop and implement accountability financial systems, processes and reporting.</span></li>
          <li><svg viewBox="0 0 12 12"><rect width="12" height="12" fill="#2d4fa6"/><path d="M3 6.2l2 2 4-4.4" stroke="#fff" stroke-width="1.6" fill="none"/></svg><span>We manage capital raising efforts, tax structuring issues and corporate transactions including mergers, acquisitions, and the sale of your business.</span></li>
        </ul>
      </div>
    </div>

    <blockquote class="quote quote--strip">If I could hire a right hand who I trust intimately to help me with financial matters, I could free up more time to run the business or work on strategy.</blockquote>

    <address class="contact">
      <div class="contact__row">
        <span class="contact__icon"><svg width="16" height="16" viewBox="0 0 16 16"><path d="M8 1.5a4.5 4.5 0 0 0-4.5 4.5c0 3.4 4.5 8.5 4.5 8.5s4.5-5.1 4.5-8.5A4.5 4.5 0 0 0 8 1.5z" fill="#fff"/><circle cx="8" cy="6" r="1.7" fill="#4aafcc"/></svg></span>
        <span class="contact__text">Tavington Inc. 1180 Brookfield Avenue SW, Calgary Alberta, Canada, T2X 4K9</span>
      </div>
      <div class="contact__row">
        <span class="contact__icon"><svg width="16" height="16" viewBox="0 0 16 16"><path d="M4 2l2.2 2.6-1.3 1.6c.9 1.9 2.3 3.3 4.2 4.2l1.6-1.3L13.3 11l-1.1 2.4C7 13.2 2.8 9 2.6 3.8z" fill="#fff"/></svg></span>
        <span class="contact__text">403 555 0148</span>
      </div>
      <div class="contact__row">
        <span class="contact__icon"><svg width="16" height="16" viewBox="0 0 16 16"><rect x="2" y="4" width="12" height="8.5" fill="#fff"/><path d="M2 4l6 4.5L14 4" stroke="#4aafcc" stroke-width="1.2" fill="none"/></svg></span>
        <span class="contact__text">mark@tavingtoninc.ca</span>
      </div>
    </address>
  </div>
</section>

</body>
</html>
```